out of the box Business Card Design for a Manufacturer / Distributor

We are a manufarturer and distributor of products.
the company name is VORTANI (Pic attached)

the picture is NOT a must have on the business Card.

the Business Card should look really professional and/or special, so out of the box thinking is welcome.

there should be 2 Adresses on the Business Card for Main and Branch Office.
Email Adress, homepage, Name is required
NO Phone Number

Our working field:
Private Labeling
high Quality Production
direct distribution
warehousing
trademark registration
legal support

Main Office:
Kornblumenweg 14
08352 Dornwiesen
Germany

Branch Office:
Daska Lane
Zarkot
Pakistan

Names:
Lukas Feldhaus (Owner)
Imran Qureshi (Owner)

Email:
lukas@vortani-example.com
imran@vortani-example.com

homepage:
vortani-example.com

Industry/Entity Type

Manufacturer Distributer

Contact Information for Business Card

Vortani

Requirements
Must have
• Names, both office Adresses, email, homepage
Should not have
• Phone Number

```html
<!DOCTYPE html>
<html lang="en">
<head>
<meta charset="utf-8">
<title>Vortani Business Card</title>
<link rel="stylesheet" href="https://fonts.googleapis.com/css2?family=Poppins:wght@300;400;500&display=swap">
<style>
  :root {
    --stage: #ececec;
    --front-top: #5a5a5a;
    --front-bottom: #3a3a3a;
    --back-top: #2e2e2e;
    --back-bottom: #1b1b1b;
    --ink: #ffffff;
    --ink-soft: #e4e4e4;
    --accent: #e3141c;
    --rule: #8a8a8a;
  }
  * { margin: 0; padding: 0; box-sizing: border-box; }
  html, body {
    width: 1200px; height: 721px; overflow: hidden;
    background: var(--stage);
    font-family: "Poppins", sans-serif;
    color: var(--ink);
  }
  .stage {
    position: relative; width: 1200px; height: 721px;
    display: flex; align-items: center; justify-content: center; gap: 48px;
  }
  .card {
    position: relative; width: 520px; height: 297px;
    box-shadow: 0 18px 40px rgba(0,0,0,0.22);
    overflow: hidden;
  }
  .card--front {
    background: linear-gradient(160deg, var(--front-top), var(--front-bottom));
    display: flex; align-items: center; justify-content: center; gap: 12px;
  }
  .brand-dot { width: 22px; height: 22px; border-radius: 50%; background: var(--ink); }
  .brand-name { font-size: 34px; font-weight: 500; letter-spacing: 4px; color: var(--ink); }

  .card--back { background: linear-gradient(160deg, var(--back-top), var(--back-bottom)); }
  .person { position: absolute; line-height: 1.05; }
  .person__name { font-size: 18px; font-weight: 500; }
  .person__name .surname { color: var(--accent); }
  .person__role { font-size: 11px; font-weight: 300; color: var(--ink-soft); margin-top: 2px; }
  .person--one { left: 34px; top: 34px; }
  .person--two { left: 280px; top: 74px; }
  .divider { position: absolute; left: 262px; top: 62px; width: 1px; height: 34px; background: var(--rule); }

  .services { position: absolute; list-style: none; font-size: 10.5px; font-weight: 400; line-height: 1.75; }
  .services li::before { content: "›"; color: var(--accent); font-weight: 500; margin-right: 10px; }
  .services--one { left: 34px; top: 108px; }
  .services--two { left: 280px; top: 142px; }

  .office { position: absolute; font-size: 10px; font-weight: 300; line-height: 1.35; color: var(--ink-soft); }
  .office__title { font-size: 12px; font-weight: 400; color: var(--ink); display: flex; align-items: center; gap: 6px; }
  .office__title svg, .contact svg { fill: var(--accent); flex: none; }
  .office__lines { padding-left: 15px; }
  .office--main { left: 34px; top: 200px; }
  .office--branch { left: 190px; top: 222px; }

  .contacts { position: absolute; left: 332px; top: 228px; font-size: 10px; font-weight: 300; line-height: 1.35; }
  .contact { display: flex; align-items: flex-start; gap: 7px; margin-bottom: 5px; }
  .contact svg { margin-top: 2px; }
</style>
</head>
<body>
<main class="stage">
  <section class="card card--front" aria-label="Card front">
    <span class="brand-dot"></span>
    <span class="brand-name">VORTANI</span>
  </section>

  <section class="card card--back" aria-label="Card back">
    <div class="person person--one">
      <div class="person__name">Lukas <span class="surname">Feldhaus</span></div>
      <div class="person__role">Owner</div>
    </div>
    <span class="divider"></span>
    <div class="person person--two">
      <div class="person__name">Imran <span class="surname">Qureshi</span></div>
      <div class="person__role">Owner</div>
    </div>

    <ul class="services services--one">
      <li>High Quality Production</li>
      <li>Direct distributiont</li>
      <li>Private Labeling</li>
    </ul>
    <ul class="services services--two">
      <li>Trademark registration</li>
      <li>Warehousing</li>
      <li>Legal suppor</li>
    </ul>

    <div class="office office--main">
      <div class="office__title">
        <svg width="9" height="11" viewBox="0 0 10 12"><path d="M5 0a4.5 4.5 0 0 0-4.5 4.5C.5 8 5 12 5 12s4.5-4 4.5-7.5A4.5 4.5 0 0 0 5 0zm0 6.3a1.8 1.8 0 1 1 0-3.6 1.8 1.8 0 0 1 0 3.6z"/></svg>
        Main Office
      </div>
      <div class="office__lines">Kornblumenweg 14, 08352<br>Dornwiesen, Germany</div>
    </div>

    <div class="office office--branch">
      <div class="office__title">
        <svg width="9" height="11" viewBox="0 0 10 12"><path d="M5 0a4.5 4.5 0 0 0-4.5 4.5C.5 8 5 12 5 12s4.5-4 4.5-7.5A4.5 4.5 0 0 0 5 0zm0 6.3a1.8 1.8 0 1 1 0-3.6 1.8 1.8 0 0 1 0 3.6z"/></svg>
        Branch Office
      </div>
      <div class="office__lines">Daska Lane, Zarkot<br>Pakistan</div>
    </div>

    <div class="contacts">
      <div class="contact">
        <svg width="9" height="9" viewBox="0 0 10 10"><circle cx="5" cy="5" r="4.5"/></svg>
        <span>www.vortani-example.com</span>
      </div>
      <div class="contact">
        <svg width="10" height="8" viewBox="0 0 10 8"><path d="M0 0h10L5 4z"/><path d="M0 1.2l5 4 5-4V8H0z"/></svg>
        <span>lukas@vortani-example.com<br>imran@vortani-example.com</span>
      </div>
    </div>
  </section>
</main>
</body>
</html>
```